Looking for someone to design a business card for my plumbing business Karvel Plumbing Solutions I want the background also to be black, must attract clients. If possible I want the front to be the logo and the back to show maybe the details.

Target Market(s)

Clients

Industry/Entity Type

Plumbing maintenance

Contact Information for Business Card

Name: Dmitri, Contact: 0437 219 608, Email: karvelplumbingsolutions@mailorix.com, Licence number 508217K

Font styles to use
Other font styles liked:
• as per logo maybe?

Colors

Designer to choose colors to be used in the design.

Requirements
Nice to have
• stating the service I provide, emergency plumbing, plumbing maintenance, drainage maintenance, block sewer and stormwater, camera and locating.

```html
<!DOCTYPE html>
<html lang="en">
<head>
<meta charset="utf-8">
<title>Karvel Plumbing Solutions – Business Card</title>
<link href="https://fonts.googleapis.com/css2?family=Figtree:wght@400;500;700;800&display=swap" rel="stylesheet">
<style>
  :root {
    --page-bg: #141414;
    --card-bg: #1e1e1e;
    --brand-blue: #4a8fd0;
    --text-light: #f2f2f2;
    --band-white: #f4f4f4;
  }
  * { margin: 0; padding: 0; box-sizing: border-box; }
  html, body {
    width: 1200px; height: 1059px; overflow: hidden;
    background: var(--page-bg);
    font-family: "Figtree", Arial, sans-serif;
    color: var(--text-light);
  }
  .canvas { position: relative; width: 1200px; height: 1059px; }
  .card {
    position: absolute;
    background: var(--card-bg);
    border-radius: 16px;
    overflow: hidden;
    box-shadow: 0 12px 28px rgba(0,0,0,0.55);
  }
  .card--details { left: 257px; top: 89px; width: 687px; height: 390px; }
  .card--logo { left: 254px; top: 547px; width: 693px; height: 393px; }

  /* Wordmark */
  .wordmark {
    position: absolute; display: flex; align-items: center;
    color: var(--text-light); font-weight: 800;
    text-transform: uppercase; line-height: 1.05;
  }
  .wordmark__dot { flex: none; border-radius: 50%; background: var(--brand-blue); }
  .card--details .wordmark { left: 40px; top: 140px; width: 270px; gap: 12px; font-size: 21px; }
  .card--details .wordmark__dot { width: 34px; height: 34px; }
  .card--logo .wordmark { left: 120px; top: 150px; width: 460px; gap: 22px; font-size: 38px; }
  .card--logo .wordmark__dot { width: 62px; height: 62px; }

  .divider {
    position: absolute; left: 323px; top: 104px;
    width: 2px; height: 152px; background: var(--brand-blue);
  }
  .contact { position: absolute; left: 350px; top: 100px; }
  .contact__name {
    color: var(--brand-blue); font-weight: 800; font-size: 26px;
    letter-spacing: 0.5px; line-height: 1; text-transform: uppercase;
  }
  .contact__role { font-size: 15.5px; line-height: 1.1; margin-top: 1px; }
  .contact__licence { font-size: 15.5px; margin-top: 13px; }
  .contact__list { list-style: none; margin-top: 10px; }
  .contact__item {
    display: flex; align-items: center; gap: 7px;
    font-size: 15.5px; height: 26.5px;
  }
  .contact__icon { width: 13px; height: 13px; flex: none; }

  .services {
    position: absolute; left: 0; right: 0; top: 309px;
    text-align: center; font-size: 15.5px; line-height: 22px;
  }
  .services__sep { color: var(--brand-blue); margin: 0 7px; }

  .accent-band { position: absolute; left: 0; bottom: 0; width: 687px; height: 14px; }
</style>
</head>
<body>
<main class="canvas">
  <section class="card card--details" aria-label="Business card – contact side">
    <div class="wordmark"><span class="wordmark__dot"></span><span>Karvel Plumbing Solutions</span></div>
    <div class="divider"></div>
    <div class="contact">
      <div class="contact__name">Dmitri</div>
      <div class="contact__role">Founder &amp; CEO</div>
      <div class="contact__licence">Licence number 508217K</div>
      <ul class="contact__list">
        <li class="contact__item">
          <svg class="contact__icon" viewBox="0 0 24 24" aria-hidden="true"><path fill="#4a8fd0" d="M6.6 10.8c1.4 2.8 3.8 5.1 6.6 6.6l2.2-2.2c.3-.3.7-.4 1-.2 1.1.4 2.3.6 3.6.6.6 0 1 .4 1 1V20c0 .6-.4 1-1 1C10.6 21 3 13.4 3 4c0-.6.4-1 1-1h3.5c.6 0 1 .4 1 1 0 1.3.2 2.5.6 3.6.1.3 0 .7-.2 1L6.6 10.8z"/></svg>
          <span>0437 219 608</span>
        </li>
        <li class="contact__item">
          <svg class="contact__icon" viewBox="0 0 24 24" aria-hidden="true"><rect x="2" y="5" width="20" height="14" rx="1" fill="#4a8fd0"/><path d="M2.5 6l9.5 7 9.5-7" fill="none" stroke="#1e1e1e" stroke-width="1.8"/></svg>
          <span>karvelplumbingsolutions@mailorix.com</span>
        </li>
        <li class="contact__item">
          <svg class="contact__icon" viewBox="0 0 24 24" aria-hidden="true"><circle cx="12" cy="12" r="11" fill="#4a8fd0"/></svg>
          <span>@KarvelPlumbingSolutions</span>
        </li>
      </ul>
    </div>
    <p class="services">
      Emergency plumbing<span class="services__sep">•</span>Plumbing maintenance<span class="services__sep">•</span>Drainage maintenance<br>
      Block sewer and stormwater<span class="services__sep">•</span>Camera and locating
    </p>
    <svg class="accent-band" viewBox="0 0 687 14" preserveAspectRatio="none" aria-hidden="true">
      <polygon points="0,0 348,0 334,14 0,14" fill="#4a8fd0"/>
      <polygon points="358,0 687,0 687,14 344,14" fill="#f4f4f4"/>
    </svg>
  </section>

  <section class="card card--logo" aria-label="Business card – logo side">
    <div class="wordmark"><span class="wordmark__dot"></span><span>Karvel Plumbing Solutions</span></div>
  </section>
</main>
</body>
</html>
```